Important Solar Energy Company Needs a Stationery Design

I need a modern, attractive, corporate stationary design (letter head and business card)
Attached Company Logo

Target Market(s)

Upmarket

Industry/Entity Type

Business

Colors
ec1f27
ffffff
757575
cbcbcb
000000

```html
<!DOCTYPE html>
<html lang="it">
<head>
<meta charset="utf-8">
<title>Solaria Prima — Letterhead</title>
<link rel="stylesheet" href="https://fonts.googleapis.com/css2?family=Lato:wght@400;700&display=swap">
<style>
  :root {
    --brand-red: #ec1f27;
    --paper: #ffffff;
    --ink: #000000;
    --ink-soft: #757575;
    --stage: #dcdcdc;
  }
  * { box-sizing: border-box; margin: 0; padding: 0; }
  html, body {
    width: 1200px;
    height: 1000px;
    overflow: hidden;
    background: var(--stage);
    font-family: "Lato", Arial, sans-serif;
  }
  .canvas {
    width: 1200px;
    height: 1000px;
    display: flex;
    align-items: center;
    justify-content: center;
  }
  .letterhead {
    position: relative;
    width: 650px;
    height: 920px;
    background: var(--paper);
    box-shadow: 0 2px 6px rgba(0,0,0,0.12);
  }
  .brand {
    position: absolute;
    top: 48px;
    left: 52px;
    display: flex;
    align-items: center;
    gap: 10px;
  }
  .brand-dot {
    width: 34px;
    height: 34px;
    border-radius: 50%;
    background: var(--brand-red);
  }
  .brand-name {
    font-size: 13px;
    font-weight: 400;
    letter-spacing: 1.5px;
    color: var(--ink);
  }
  .footer {
    position: absolute;
    right: 52px;
    bottom: 46px;
    display: flex;
    align-items: flex-end;
    gap: 26px;
  }
  .footer-company .company-name {
    font-size: 11px;
    letter-spacing: 1.4px;
    color: var(--ink);
    margin-bottom: 3px;
  }
  .footer-company address,
  .footer-contacts {
    font-style: normal;
    font-size: 8px;
    line-height: 1.45;
    color: var(--ink-soft);
  }
  .footer-contacts dt {
    display: inline;
    font-weight: 700;
    color: var(--brand-red);
  }
  .footer-contacts dd {
    display: inline;
    margin: 0;
  }
  .footer-contacts dd::after { content: ""; display: block; }
</style>
</head>
<body>
  <main class="canvas">
    <article class="letterhead">
      <header class="brand">
        <span class="brand-dot" aria-hidden="true"></span>
        <span class="brand-name">SOLARIA PRIMA</span>
      </header>

      <footer class="footer">
        <div class="footer-company">
          <p class="company-name">SOLARIA PRIMA</p>
          <address>
            Via dei Girasoli, 24<br>
            64010 Marina Alta TE
          </address>
        </div>
        <dl class="footer-contacts">
          <dt>Tel:</dt> <dd>+39 0185 320 4100</dd>
          <dt>Fax:</dt> <dd>+39 0185 320 4102</dd>
          <dt>Web:</dt> <dd>www.solariaprima.it</dd>
          <dt>Email:</dt> <dd>ciao@solariaprima.it</dd>
        </dl>
      </footer>
    </article>
  </main>
</body>
</html>
```